Brindle Works Australia Website

Brindle Works Australia (BWA) is a Industrial, Mining & Transport Services provider in Australia. We require a website that is both pc and mobile freindly. The website will be used to both present our company services and give us exposure in a crowded market. The main page of the website will have a snapshot of who BWA is and its from this page that the user can click to enter the area of interest ie. Industrial, Mining and Transport. A disticted logo can be used to indicate the area in question.<br/>Within the industrial, Mining and the Transport services pages will need list and description of services that are provided, current customer lists and news pages.<br/>The website will need a contacts page so prospective customers can get in contact with BWA.<br/>The website design will require a user freindly back end so future updates and ammendments can be carriedout by less experienced people within the BWA business.

Target Market(s)

Industrial, Mining and Transport Services provider markets

Coding

Coded - Design and coding required

Number of Pages Required

5+ page

Font styles to use
Sans Serif

Colors
00a990

Requirements
Must have
• Ability to build servises with in services. because the main service area is only the main service with in each service group there is alot of smaller services / tasks.
• Key wording for easy seach engine capabilities. The website will need to be search engine freindly.

```html
<!DOCTYPE html>
<html lang="en">
<head>
<meta charset="utf-8">
<title>Brindle Works Australia – Industrial, Mining &amp; Transport Services</title>
<link href="https://fonts.googleapis.com/css2?family=Poppins:wght@300;400;500;600&display=swap" rel="stylesheet">
<style>
:root{
  --green:#0b6f32;
  --green-band:#0b7e3d;
  --green-footer:#096a33;
  --navy:#0c2239;
  --ink:#1f2a36;
  --muted:#6d7480;
  --pale:#f4f8fd;
  --white:#ffffff;
  --red:#c4161c;
  --icon-grey:#e3e6ea;
  --partner-grey:#737373;
}
*{margin:0;padding:0;box-sizing:border-box}
html,body{width:1200px;height:2678px;overflow:hidden}
body{font-family:"Poppins",sans-serif;color:var(--ink);background:var(--white);position:relative}
.abs{position:absolute}
.btn{position:absolute;background:var(--green);color:var(--white);font-size:14px;font-weight:500;letter-spacing:1.5px;display:flex;align-items:center;justify-content:center}

/* hero */
.hero{left:0;top:0;width:1200px;height:493px;
  background:
    radial-gradient(ellipse 260px 200px at 90px 150px,rgba(96,140,70,.95),rgba(96,140,70,0) 75%),
    radial-gradient(ellipse 220px 110px at 380px 70px,rgba(110,150,80,.8),rgba(110,150,80,0) 80%),
    radial-gradient(ellipse 180px 140px at 400px 290px,rgba(170,40,60,.55),rgba(170,40,60,0) 80%),
    radial-gradient(ellipse 140px 190px at 650px 300px,rgba(225,228,232,.55),rgba(225,228,232,0) 80%),
    radial-gradient(ellipse 200px 320px at 1120px 320px,rgba(170,160,100,.75),rgba(170,160,100,0) 80%),
    radial-gradient(ellipse 180px 120px at 1060px 40px,rgba(80,130,90,.7),rgba(80,130,90,0) 80%),
    linear-gradient(180deg,#6f7b78 0%,#545c64 40%,#4a525a 100%)}
.hero-shade{left:0;top:0;width:1200px;height:493px;background:rgba(20,40,70,.18)}
.brand{left:36px;top:30px;display:flex;align-items:center;gap:8px;color:var(--white);font-weight:600;font-size:15px;line-height:1.05}
.brand-mark{width:28px;height:28px;background:var(--white)}
.nav{left:432px;top:42px;display:flex;gap:41px;color:var(--white);font-size:15px;font-weight:500}
.nav span.drop::after{content:"";display:inline-block;width:6px;height:6px;border-right:1.2px solid #fff;border-bottom:1.2px solid #fff;transform:rotate(45deg);margin:0 0 3px 6px}
.hero-title{left:80px;top:184px;font-size:57px;font-weight:600;color:var(--white);line-height:1.2}
.strip{left:0;top:493px;width:1200px;height:22px;background:linear-gradient(90deg,#3f4a5d,#5b6478 20%,#7a6c52 40%,#c59a4a 55%,#48516a 75%,#6a7080)}

/* services */
.svc-photo{left:0;top:515px;width:395px;height:667px;
  background:
    radial-gradient(ellipse 170px 110px at 200px 170px,rgba(235,238,242,.9),rgba(235,238,242,0) 75%),
    radial-gradient(ellipse 140px 70px at 330px 90px,rgba(225,230,238,.8),rgba(225,230,238,0) 80%),
    radial-gradient(ellipse 60px 260px at 70px 500px,rgba(150,120,90,.65),rgba(150,120,90,0) 85%),
    radial-gradient(ellipse 50px 280px at 345px 470px,rgba(190,170,140,.7),rgba(190,170,140,0) 85%),
    radial-gradient(ellipse 40px 220px at 230px 470px,rgba(150,110,80,.6),rgba(150,110,80,0) 85%),
    linear-gradient(180deg,#4c6596 0%,#5b6f98 40%,#535c72 70%,#3b3e44 100%)}
.svc-title{font-size:24px;font-weight:400;line-height:1.2}
.svc-icon{background:var(--icon-grey)}

/* about */
.about{left:0;top:1215px;width:1200px;height:495px;background:var(--pale)}
.frame{background:var(--white)}
.about-h{left:690px;top:1233px;width:490px;font-size:39px;font-weight:500;line-height:45px;color:var(--navy)}
.about-p{left:690px;top:1420px;width:510px;font-size:14.5px;font-weight:300;line-height:26px;color:var(--muted);letter-spacing:-.1px}
.bar{position:absolute;left:690px;font-size:15px;color:var(--navy);border-bottom:3px solid var(--navy);display:flex;justify-content:space-between;padding-bottom:8px}

/* testimonial */
.testi{left:0;top:1710px;width:1200px;height:424px;
  background:
    radial-gradient(ellipse 150px 260px at 170px 220px,rgba(120,140,170,.45),rgba(120,140,170,0) 80%),
    radial-gradient(ellipse 120px 140px at 790px 120px,rgba(120,120,130,.35),rgba(120,120,130,0) 80%),
    linear-gradient(100deg,#3e5068 0%,#46586f 45%,#2f3847 72%,#2a313c 100%)}
.quote{left:0;top:1880px;width:1200px;text-align:center;color:var(--white);font-size:19px;line-height:30px}
.arrow{width:46px;height:46px;border-radius:50%;display:flex;align-items:center;justify-content:center}

/* partners */
.partner{background:var(--partner-grey)}

/* newsletter & footer */
.news{left:0;top:2290px;width:1200px;height:96px;background:var(--green-band)}
.news-h{left:80px;top:2321px;color:var(--white);font-size:29px;font-weight:500;line-height:1.2}
.mail{left:614px;top:2317px;width:400px;height:42px;background:var(--white);color:#8a8f96;font-size:15px;padding:0 18px;display:flex;align-items:center}
.sub{left:1014px;top:2317px;width:107px;height:42px;background:var(--red);color:var(--white);font-size:14px;display:flex;align-items:center;justify-content:center}
.footer{left:0;top:2386px;width:1200px;height:292px;background:var(--green-footer)}
.fcol{color:var(--white)}
.fcol h4{font-size:17px;font-weight:500;margin-bottom:30px}
.fcol p{font-size:12px;line-height:19px;color:#e6f0ea}
.copy{left:0;top:2637px;width:1200px;text-align:center;font-size:13px;color:#c9b98a}
</style>
</head>
<body>

<!-- hero -->
<div class="abs hero" role="img" aria-label="Photo of freight trucks driving on a highway"></div>
<div class="abs hero-shade"></div>
<div class="abs brand"><div class="brand-mark"></div><div>Brindle Works<br>Australia</div></div>
<nav class="abs nav">
  <span>Home</span><span class="drop">Industrial Services</span><span class="drop">Mining Services</span><span class="drop">Transport</span><span>Contact</span>
</nav>
<h1 class="abs hero-title">Mining Services</h1>
<div class="btn" style="left:80px;top:280px;width:179px;height:47px">Know More</div>
<div class="abs strip" role="img" aria-label="Strip of industrial photography"></div>

<!-- services -->
<div class="abs svc-photo" role="img" aria-label="Photo of power plant chimneys with smoke at dusk"></div>
<h2 class="abs svc-title" style="left:96px;top:577px;color:#fff">Industrial Services</h2>
<div class="btn" style="left:104px;top:891px;width:180px;height:46px">Know More</div>
<div class="abs" style="left:112px;top:960px;width:170px;height:160px;background:rgba(225,228,232,.45);border-radius:8px" role="img" aria-label="Faint factory icon"></div>

<h2 class="abs svc-title" style="left:480px;top:575px">Mining Services</h2>
<div class="btn" style="left:479px;top:918px;width:180px;height:47px">Know More</div>
<div class="abs svc-icon" style="left:482px;top:1010px;width:236px;height:138px;border-radius:30px 30px 16px 16px" role="img" aria-label="Faint bulldozer icon"></div>

<h2 class="abs svc-title" style="left:880px;top:575px">Transport Services</h2>
<div class="btn" style="left:879px;top:891px;width:180px;height:47px">Know More</div>
<div class="abs svc-icon" style="left:882px;top:954px;width:230px;height:168px;border-radius:40px 16px 30px 30px" role="img" aria-label="Faint truck icon"></div>

<!-- about -->
<section class="abs about"></section>
<div class="abs frame" style="left:12px;top:1422px;width:434px;height:290px"></div>
<div class="abs" style="left:23px;top:1434px;width:410px;height:264px;background:radial-gradient(ellipse 120px 90px at 290px 150px,rgba(230,150,60,.55),rgba(230,150,60,0) 80%),linear-gradient(180deg,#2c2f38 0%,#5a4028 50%,#c77a2c 80%,#3a2a1c 100%)" role="img" aria-label="Photo of a bucket-wheel excavator at sunset"></div>
<div class="abs frame" style="left:172px;top:1228px;width:416px;height:266px"></div>
<div class="abs" style="left:185px;top:1240px;width:391px;height:241px;background:radial-gradient(ellipse 140px 80px at 260px 190px,rgba(220,150,70,.5),rgba(220,150,70,0) 80%),linear-gradient(180deg,#c7c3d8 0%,#e6c3b0 40%,#8a6d62 70%,#3e3f4a 100%)" role="img" aria-label="Photo of an industrial refinery at dawn"></div>
<h2 class="abs about-h">We provide best services from ever-growing Industrial, Mining &amp; Transport.</h2>
<p class="abs about-p">Aenean sollicitudin, lorem quis bibendum auctor, nisi elit consequat ipsum, nec sagittis sem nibh id elit duis sed odio sit amet.</p>
<div class="bar" style="top:1497px;width:485px"><span>Latest Equipemnts Used</span><span>95%</span></div>
<div class="bar" style="top:1550px;width:408px"><span>Factories Production</span><span>80%</span></div>
<div class="bar" style="top:1603px;width:357px"><span>Management &amp; Services</span><span>70%</span></div>

<!-- testimonial -->
<section class="abs testi" role="img" aria-label="Photo of a man working at a desk by a window"></section>
<svg class="abs" style="left:577px;top:1804px" width="46" height="34" viewBox="0 0 46 34"><path d="M0 0h18v16l-12 18h-6zM28 0h18v16l-12 18h-6z" fill="#fff"/></svg>
<p class="abs quote">Donec imperdiet congue orci consequat mattis. Donec rutrum porttitor sollicitudin. Pellentesque id dolor<br>tempor sapien feugiat ultrices nec sed neque. Fusce ac mattis nulla. Morbi eget ornare dui.</p>
<div class="abs arrow" style="left:80px;top:1908px"><svg width="12" height="14" viewBox="0 0 12 14"><path d="M8 1 3 7l5 6" stroke="#fff" stroke-width="1.6" fill="none"/></svg></div>
<div class="abs arrow" style="left:1073px;top:1908px;border:1px solid rgba(255,255,255,.5)"><svg width="12" height="14" viewBox="0 0 12 14"><path d="M4 1l5 6-5 6" stroke="#fff" stroke-width="1.6" fill="none"/></svg></div>
<div class="abs" style="left:580px;top:1962px;width:40px;height:40px;border-radius:50%;background:#d9d4cf" role="img" aria-label="Client portrait"></div>
<div class="abs" style="left:0;top:2012px;width:1200px;text-align:center;color:#fff;font-size:14px;font-weight:500">Dale Merriwether</div>
<div class="abs" style="left:0;top:2040px;width:1200px;text-align:center;color:#fff;font-size:12px">Business Owner</div>

<!-- partners -->
<div class="abs partner" style="left:113px;top:2175px;width:72px;height:74px;border-radius:10px"></div>
<div class="abs partner" style="left:200px;top:2198px;width:108px;height:26px;border-radius:4px;opacity:.85"></div>
<div class="abs partner" style="left:426px;top:2152px;width:92px;height:92px;border-radius:50%"></div>
<div class="abs partner" style="left:408px;top:2252px;width:126px;height:20px;border-radius:4px;opacity:.85"></div>
<div class="abs partner" style="left:683px;top:2172px;width:98px;height:76px;border-radius:38px"></div>
<div class="abs partner" style="left:935px;top:2155px;width:116px;height:116px;border-radius:50%"></div>

<!-- newsletter -->
<section class="abs news"></section>
<h3 class="abs news-h">Stay Updated With Our Newsletter</h3>
<div class="abs mail">Enter your mail</div>
<div class="abs sub">Subscribe</div>

<!-- footer -->
<footer class="abs footer"></footer>
<div class="abs fcol" style="left:80px;top:2443px">
  <h4>Industrial Services</h4>
  <p>Field Services Units<br>Onsite Breakdown Services<br>Generator Rental<br>Preventive Maintenance Plans<br>Plant Decommissioning &amp; Relocation</p>
</div>
<div class="abs fcol" style="left:347px;top:2443px">
  <h4>Mining Services</h4>
  <p>Field Services Units<br>Onsite Breakdown Services<br>Onsite Mechanical Services</p>
</div>
<div class="abs fcol" style="left:614px;top:2443px">
  <h4>Transport</h4>
  <p>About<br>Blog<br>Contact<br>Appointment</p>
</div>
<div class="abs fcol" style="left:881px;top:2443px">
  <h4>Address</h4>
  <p style="line-height:26px">412/B, Quarry Lane, Stonebridge<br>Vale-5120</p>
  <p>+61 400 118 274<br>hello@brindleworks.example</p>
</div>
<div class="abs copy">Copyright ©2020 All rights reserved</div>

</body>
</html>
```